Logo Design - Wine Range

Hello Designers,
We need a graphic design for a new logo for a wine range that we are releasing in coming months and are wanting to design a logo that reflects the name in a unique and creative way.
The Name is HERON GLEN.
We are really wanting the Logo/label to have a visual element which in a quick glance it is visually symbolic and one to remember.
Brief
A )Label with be 10 cm length and 9cm width, wanting picture to be about 5cm in Length. Information on the front label needs to be Name - Heron Glen
B) Looking for BRIGHT AND BOLD colours that attract and relate to Australian Nature. Can also include Falcon Bird but not necessary.
The designer who is selected as winner will need to create a label in order to complete the project. Goodluck :)
Thank you for your interest, looking forward to reviewing designs soon.
Updates
Label with be 10 cm length and 9cm width, wanting picture to be about 5cm in Length. Information on the front label needs to be Name - Heron Glen
have attached a colour palette of Australian Nature for an idea of colour.
Target Market(s)
Age group 18+
Industry/Entity Type
Graphic Design
Requirements
Must have
- Must include a graphic design not just words
Nice to have
- Unique and modern touch, If using Falcon would like the bird to be whole, Australian Nature. Rocks, waterfalls... the sky is the limit really , goodluck

```html
<!DOCTYPE html>
<html lang="en">
<head>
<meta charset="utf-8">
<title>Heron Glen – Cabernet Sauvignon Label</title>
<link rel="stylesheet" href="https://fonts.googleapis.com/css2?family=Cormorant+Garamond:wght@500&family=Cormorant+SC:wght@500&family=Tenor+Sans&display=swap">
<style>
  :root {
    --canvas-bg: #f4eee2;
    --label-sand: #d5bf9c;
    --label-sand-light: #eadfcb;
    --label-white: #fbfbfa;
    --rule-blue: #a9c3de;
    --rule-gold: #c8a878;
    --ink: #2a2622;
    --ink-soft: #4a4540;
    --sky-light: #dce8f7;
    --sky-mid: #a9c2e8;
    --sky-deep: #7f9fd2;
  }
  * { margin: 0; padding: 0; box-sizing: border-box; }
  html, body {
    width: 960px;
    height: 1200px;
    overflow: hidden;
    background: var(--canvas-bg);
  }
  .canvas {
    position: relative;
    width: 960px;
    height: 1200px;
    display: flex;
    align-items: center;
    justify-content: center;
  }
  .wine-label {
    position: relative;
    width: 545px;
    height: 792px;
    background: linear-gradient(to bottom,
      var(--label-sand) 0%,
      var(--label-sand-light) 14%,
      var(--label-white) 34%,
      var(--label-white) 58%,
      var(--label-sand-light) 80%,
      var(--label-sand) 100%);
    box-shadow: 0 4px 18px rgba(80, 60, 30, 0.12);
    text-align: center;
    color: var(--ink);
  }
  .wine-label::before,
  .wine-label::after {
    content: "";
    position: absolute;
    left: 0;
    right: 0;
    height: 4px;
    background: linear-gradient(to bottom, var(--rule-gold), var(--rule-blue));
  }
  .wine-label::before { top: 6px; }
  .wine-label::after { bottom: 6px; }
  .origin {
    position: absolute;
    top: 40px;
    left: 0;
    right: 0;
    font-family: "Cormorant SC", "Times New Roman", serif;
    font-weight: 500;
    font-size: 24px;
    letter-spacing: 1px;
    color: var(--ink-soft);
  }
  .brand-name {
    position: absolute;
    top: 214px;
    left: 0;
    right: 0;
    font-family: "Cormorant Garamond", "Times New Roman", serif;
    font-weight: 500;
    font-size: 78px;
    line-height: 1;
    color: var(--ink);
  }
  .varietal {
    position: absolute;
    top: 318px;
    left: 0;
    right: 0;
    font-family: "Tenor Sans", Arial, sans-serif;
    font-size: 24px;
    letter-spacing: 1px;
    color: var(--ink);
  }
  .bird-artwork {
    position: absolute;
    top: 392px;
    left: 152px;
    width: 241px;
    height: 290px;
  }
  .sky-top { stop-color: var(--sky-light); }
  .sky-middle { stop-color: var(--sky-mid); }
  .sky-bottom { stop-color: var(--sky-deep); }
  .appellation {
    position: absolute;
    top: 720px;
    left: 0;
    right: 0;
    font-family: "Cormorant SC", "Times New Roman", serif;
    font-weight: 500;
    font-size: 16px;
    line-height: 22px;
    letter-spacing: 0.6px;
    color: var(--ink-soft);
  }
</style>
</head>
<body>
  <main class="canvas">
    <section class="wine-label">
      <p class="origin">Product of Australia</p>
      <h1 class="brand-name">Heron Glen</h1>
      <p class="varietal">CABERNET SAUVIGNON</p>
      <svg class="bird-artwork" role="img" aria-label="Silver-blue illustration of a bird in flight with wings raised" viewBox="0 0 241 290">
        <defs>
          <linearGradient id="sky-fill" x1="0" y1="0" x2="0.4" y2="1">
            <stop offset="0%" class="sky-top"/>
            <stop offset="55%" class="sky-middle"/>
            <stop offset="100%" class="sky-bottom"/>
          </linearGradient>
        </defs>
        <rect x="0" y="0" width="241" height="290" rx="24" fill="url(#sky-fill)"/>
      </svg>
      <p class="appellation">Protected Geographical Indication<br>Traditional Speciality Guaranteed</p>
    </section>
  </main>
</body>
</html>
```